Compression Arm Sleeve Packaging

We are a seller of sports compression arm sleeves. Our arm sleeves are used by athletes in just about every sport. Baseball, football, & basketball make up our largest customer base. We are in need of a product packaging design as a Vector image.

We would like design to feature the following:
Front of package:
Name of product: Arm Sleeve, our logo, brand name, website address, center of package will need to have no content so sleeve can be seen through package.

Back of package: Size chart, website address, logo, brand name, product care:
Machine Wash <80F
Do Not Dry Clean
Do Not Iron
Do Not Bleach
Hang Dry

I have included a few samples of other arm sleeve brands packaging. The plomets package i like the "Plomets" scrolling across package, the kvorex package i like the different colors, although I would not want the same colors, The zentarig i like that the name of company, & the item are in bold. I do not like the basketball player on the front.

Misc Notes. I have included a pic of our logo, as well as our brand name. The font used for our brand name can be changed. The color of logo can also be changed if needed. Also i have attached a picture of our website name. The measurement chart does not need to look exactly as one i posted.
Thank you for looking!!!

Target Market(s)

Athletes - Youth & adult

Font styles to use
Sans Serif

Requirements
Must have
• Brand Name - Tarnhollow Athletics
• Website: tarnhollowathletics.example
• Logo
• Measurement chart (back of package)
• Product Care (back of package)
• I am very open to colors. I see i have to choose color combos. Regardless of the colors i choose I am not a designer. Use your judgement on what you think works.
Nice to have
• Would like a package where the color really pops. If our arm sleeve package is placed beside 10 other arm sleeve brands packaging I want to be sure our package would be the one that stands out without being corny. Packaging should appeal to extreme athletes. Font - Our font is Vexa Goalline, however it is not my favorite. If you have something you think looks better go with it. Again if i was a designer you would not be reading this. Create a package that you think will stand out to extreme athletes, and at the same time the future extreme athletes.
Should not have
• Boring packaging.

```html
<!DOCTYPE html>
<html lang="en">
<head>
<meta charset="utf-8">
<title>Tarnhollow Athletics – Arm Sleeve Package Front</title>
<link rel="stylesheet" href="https://fonts.googleapis.com/css2?family=Michroma&family=Ubuntu:wght@300;400&display=swap">
<style>
  :root {
    --page-bg: #e6e6e6;
    --brand-red: #e30a17;
    --brand-red-deep: #c9141a;
    --brand-blue: #039be0;
    --brand-blue-deep: #0a8ed3;
    --window-white: #ffffff;
    --ink-light: #ffffff;
    --rule-light: #bfe6fa;
  }
  html, body {
    margin: 0;
    width: 1200px;
    height: 1200px;
    overflow: hidden;
    background: var(--page-bg);
  }
  .package-front {
    position: absolute;
    left: 205px;
    top: 40px;
    width: 790px;
    height: 1120px;
    display: block;
  }
  .site-url {
    font-family: "Ubuntu", sans-serif;
    font-weight: 300;
    fill: var(--ink-light);
  }
  .brand-name,
  .tagline,
  .product-name,
  .feature-note,
  .feature-label {
    font-family: "Michroma", sans-serif;
    fill: var(--ink-light);
  }
  .brand-name { font-size: 30px; letter-spacing: 2px; }
  .tagline { font-size: 30px; letter-spacing: 8px; }
  .product-name { font-size: 80px; stroke: var(--ink-light); stroke-width: 2.5px; }
  .feature-note { font-size: 20px; letter-spacing: 1.5px; }
  .feature-label { font-size: 15px; }
  .headline-rule { stroke: var(--rule-light); stroke-width: 1.5; }
  .icon-disc { fill: var(--ink-light); }
  .icon-mark { fill: var(--brand-blue); }
  .icon-line { stroke: var(--brand-blue); stroke-width: 2; fill: none; }
</style>
</head>
<body>
<svg class="package-front" viewBox="0 0 830 1177" xmlns="http://www.w3.org/2000/svg" aria-labelledby="pkg-title">
  <title id="pkg-title">Tarnhollow Athletics arm sleeve package, front</title>
  <defs>
    <linearGradient id="red-field" x1="0" y1="0" x2="1" y2="1">
      <stop offset="0" stop-color="var(--brand-red)"/>
      <stop offset="1" stop-color="var(--brand-red-deep)"/>
    </linearGradient>
    <linearGradient id="blue-field" x1="0" y1="0" x2="1" y2="1">
      <stop offset="0" stop-color="var(--brand-blue)"/>
      <stop offset="1" stop-color="var(--brand-blue-deep)"/>
    </linearGradient>
    <filter id="band-shadow" x="-5%" y="-5%" width="110%" height="120%">
      <feDropShadow dx="0" dy="4" stdDeviation="4" flood-color="#000" flood-opacity="0.25"/>
    </filter>
  </defs>

  <!-- clear window for the sleeve -->
  <rect class="sleeve-window" width="830" height="1177" fill="var(--window-white)"/>

  <!-- lower blue band -->
  <path class="band-lower" role="img" aria-label="Blue band with hexagon texture"
        fill="url(#blue-field)"
        d="M0,530 C60,560 110,582 150,595 C250,625 350,645 440,665 C462,668 482,660 520,645 C640,608 740,580 830,545 L830,1177 L0,1177 Z"/>

  <!-- upper red band -->
  <path class="band-upper" role="img" aria-label="Red band with hexagon texture"
        fill="url(#red-field)" filter="url(#band-shadow)"
        d="M0,0 L830,0 L830,190 C720,250 600,310 480,385 C462,396 455,398 445,395 C300,360 100,340 0,300 Z"/>

  <!-- header -->
  <text class="site-url" x="412" y="88" text-anchor="middle" font-size="30">www.tarnhollowathletics.example</text>
  <text class="brand-name" x="415" y="200" text-anchor="middle">TARNHOLLOW</text>
  <text class="brand-name" x="415" y="248" text-anchor="middle">ATHLETICS</text>

  <!-- product title -->
  <text class="tagline" x="422" y="770" text-anchor="middle" textLength="595" lengthAdjust="spacingAndGlyphs">★ATHLETES CHOICE★</text>
  <text class="product-name" x="412" y="847" text-anchor="middle" textLength="722" lengthAdjust="spacingAndGlyphs">ARM SLEEVE</text>
  <line class="headline-rule" x1="93" y1="861" x2="726" y2="861"/>
  <text class="feature-note" x="415" y="890" text-anchor="middle" textLength="505" lengthAdjust="spacingAndGlyphs">WITH OUR REINFORCED NON-SLIP</text>
  <text class="feature-note" x="414" y="918" text-anchor="middle" textLength="368" lengthAdjust="spacingAndGlyphs">SILICONE ELASTIC BAND</text>

  <!-- features -->
  <g class="feature feature-compression">
    <circle class="icon-disc" cx="149" cy="1022" r="49"/>
    <path class="icon-line" d="M130,996 L150,1044 L178,1034"/>
    <path class="icon-mark" d="M126,986 L140,994 L131,999 Z"/>
    <path class="icon-line" d="M160,1040 L172,1016 M166,1038 L176,1020"/>
    <text class="feature-label" x="149" y="1105" text-anchor="middle">OVERALL</text>
    <text class="feature-label" x="149" y="1125" text-anchor="middle">COMPRESSION</text>
  </g>
  <g class="feature feature-wicking">
    <circle class="icon-disc" cx="420" cy="1022" r="49"/>
    <path class="icon-mark" d="M420,990 C410,1008 396,1022 396,1037 A24,24 0 0 0 444,1037 C444,1022 430,1008 420,990 Z"/>
    <path d="M408,1036 L432,1036 L420,1048 Z" fill="var(--ink-light)"/>
    <text class="feature-label" x="420" y="1105" text-anchor="middle">MOISTURE</text>
    <text class="feature-label" x="420" y="1125" text-anchor="middle">WICKING MATERIAL</text>
  </g>
  <g class="feature feature-seam">
    <circle class="icon-disc" cx="690" cy="1022" r="49"/>
    <line class="icon-line" x1="655" y1="1057" x2="725" y2="987" stroke-dasharray="6 5"/>
    <text class="feature-label" x="688" y="1105" text-anchor="middle">FLAT SEAM</text>
    <text class="feature-label" x="688" y="1125" text-anchor="middle">TECHNOLOGY</text>
  </g>
</svg>
</body>
</html>
```